I need a business card for myself, being a proprietor of a funeral parlor based in Manila. I'd like the card to have either of the following:
White Font on Black Background
or
Black Font on White Background
No logo is needed however I will appreciate any efforts to show a symbol of eternal happiness, aptly designed with above mentioned colors in mind.
Company name, address and contact on the lower right corner.
Logo or symbol anywhere.
Quillstone Funeral Services
+639174826351
darvik4521@pelmora.com
corner of Brisco Avenue and Velhurst Street
Makati City, Philippines
Thank you.
Update: Please include a small dove in your design. You are free to choose where you would like it on the card.

```html
<!DOCTYPE html>
<html lang="en">
<head>
<meta charset="utf-8">
<title>Quillstone Funeral Services – Business Cards</title>
<link rel="stylesheet" href="https://fonts.googleapis.com/css2?family=Playfair+Display:wght@400;700&family=Mulish:wght@400;600&display=swap">
<style>
  :root {
    --ink: #000000;
    --paper: #ffffff;
    --stage: #ffffff;
    --mark-on-dark: #ffffff;
    --mark-on-light: #000000;
    --shadow: rgba(0, 0, 0, 0.22);
  }
  * { margin: 0; padding: 0; box-sizing: border-box; }
  html, body { width: 1200px; height: 901px; overflow: hidden; background: var(--stage); }
  .stage { position: relative; width: 1200px; height: 901px; }

  .card {
    position: absolute;
    width: 522px;
    height: 318px;
    box-shadow: 0 2px 10px var(--shadow);
    text-align: center;
    overflow: hidden;
  }
  .card--dark { background: var(--ink); color: var(--paper); }
  .card--light { background: var(--paper); color: var(--ink); }

  .card--banded { left: 339px; top: 72px; }
  .card--classic-light { left: 58px; top: 483px; }
  .card--classic-dark { left: 619px; top: 483px; }

  .brand-dot {
    position: absolute;
    left: 50%;
    top: 42px;
    width: 66px;
    height: 66px;
    transform: translateX(-50%);
    border-radius: 50%;
  }
  .card--dark .brand-dot { background: var(--mark-on-dark); }
  .card--light .brand-dot { background: var(--mark-on-light); }

  .company-name {
    position: absolute;
    left: 0; right: 0;
    top: 118px;
    font-family: "Playfair Display", serif;
    font-weight: 400;
    font-size: 52px;
    line-height: 1;
    letter-spacing: 0.5px;
  }
  .company-tagline {
    position: absolute;
    left: 0; right: 0;
    top: 176px;
    padding-left: 6px;
    font-family: "Playfair Display", serif;
    font-weight: 700;
    font-size: 24px;
    line-height: 1;
    letter-spacing: 6px;
  }

  .contact-band {
    position: absolute;
    left: 0; right: 0;
    top: 239px;
    height: 53px;
    background: var(--paper);
    color: var(--ink);
    font-family: "Mulish", sans-serif;
    font-size: 13.5px;
    line-height: 21px;
    padding-top: 6px;
  }
  .contact-band strong { font-weight: 600; }

  .contact {
    position: absolute;
    left: 0; right: 0;
    top: 257px;
    font-family: "Playfair Display", serif;
    font-size: 13.5px;
    line-height: 20px;
  }
</style>
</head>
<body>
<main class="stage">

  <section class="card card--dark card--banded">
    <div class="brand-dot" aria-hidden="true"></div>
    <h1 class="company-name">QUILLSTONE</h1>
    <p class="company-tagline">FUNERAL SERVICES</p>
    <div class="contact-band">
      <p>PHONE <strong>+639 174 826 351</strong>&nbsp; EMAIL <strong>darvik4521@pelmora.com</strong></p>
      <p>Corner of Brisco Avenue and Velhurst Street Makati City, Philippines</p>
    </div>
  </section>

  <section class="card card--light card--classic-light">
    <div class="brand-dot" aria-hidden="true"></div>
    <h1 class="company-name">QUILLSTONE</h1>
    <p class="company-tagline">FUNERAL SERVICES</p>
    <div class="contact">
      <p>PHONE +639 174 826 351&nbsp; EMAIL darvik4521@pelmora.com</p>
      <p>Corner of Brisco Avenue and Velhurst Street Makati City, Philippines</p>
    </div>
  </section>

  <section class="card card--dark card--classic-dark">
    <div class="brand-dot" aria-hidden="true"></div>
    <h1 class="company-name">QUILLSTONE</h1>
    <p class="company-tagline">FUNERAL SERVICES</p>
    <div class="contact">
      <p>PHONE +639 174 826 351&nbsp; EMAIL darvik4521@pelmora.com</p>
      <p>Corner of Brisco Avenue and Velhurst Street Makati City, Philippines</p>
    </div>
  </section>

</main>
</body>
</html>
```